Creative modern Trade show booth design for saas software company

We are looking for a simple clean Trade show booth design for our booth. The dimension of the booth are attached for reference. samples of other designs we like are also attached. Our website is in www.trelvix.com. The both consists of two-piece main booth back, a stand and an iPad stand. The booth design showing the Monkey on it is the booth. We would like our logo shown, possibly an image and short description of our services. and maybe images of our reports. please visit our website to get ideas. our main product is Trelvix Software.

Target Market(s)

Insurance agents/ brokers & producers.

Font styles to use
Other font styles liked:
• abadi MT Pro

Colors

Designer to choose colors to be used in the design.

Requirements
Must have
• Our Logo. A creative statement to draw attention. Our 4 sectors of products. Trelvix Software, Trelvix Claims, Trelvix Markets, Trelvix Products

```html
<!DOCTYPE html>
<html lang="en">
<head>
<meta charset="utf-8">
<title>Trelvix Trade Show Booth Set</title>
<link rel="stylesheet" href="https://fonts.googleapis.com/css2?family=Montserrat:wght@400;500;600;700;800&family=Oswald:wght@500;600&display=swap">
<style>
  :root{
    --brand-blue:#1f9cc8;
    --brand-blue-light:#27b0dd;
    --brand-dark:#3b4045;
    --panel-white:#f1f2f3;
    --panel-grey:#e3e5e7;
    --bg-dark:#353535;
    --bg-light:#9a9a9a;
  }
  *{box-sizing:border-box;margin:0;padding:0}
  html,body{width:1200px;height:480px;overflow:hidden}
  body{
    position:relative;
    background:linear-gradient(100deg,var(--bg-dark) 0%,#6a6a6a 45%,var(--bg-light) 100%);
    font-family:"Montserrat",sans-serif;
  }
  .piece{position:absolute}
  .wordmark{font-family:"Montserrat",sans-serif;font-weight:600;color:var(--brand-blue);letter-spacing:.5px;line-height:1}

  /* Left banner */
  .side-banner{left:39px;top:49px;width:131px;height:382px;background:linear-gradient(160deg,var(--brand-blue-light),#1b86ad)}
  .side-banner .badge{
    position:absolute;left:20px;top:48px;width:90px;height:90px;border-radius:50%;
    background:#fff;border:2px solid #fff;box-shadow:0 0 0 2px var(--brand-blue),0 0 0 3px #fff;
    display:flex;align-items:center;justify-content:center;text-align:center;
    font-weight:700;font-size:11px;line-height:12.5px;color:var(--brand-dark)
  }

  /* Monitor */
  .monitor{left:107px;top:192px;width:132px;height:82px;background:#1d1f22;border-radius:2px;padding:3px 3px 7px}
  .monitor .screen{width:100%;height:100%;background:#fff;display:flex;flex-direction:column;align-items:center;justify-content:center;gap:6px}
  .monitor .wordmark{font-size:17px}
  .monitor .url{font-size:5px;color:var(--brand-dark)}

  /* Header sign */
  .header-sign{left:205px;top:85px;width:197px;height:48px;background:linear-gradient(135deg,#f6f6f6,var(--panel-grey));display:flex;align-items:center;justify-content:center}
  .header-sign .wordmark{font-size:30px}

  /* Poster */
  .poster{left:176px;top:140px;width:255px;height:291px;background:linear-gradient(160deg,#fafafa,var(--panel-grey));overflow:hidden}
  .poster .photo{position:absolute;left:150px;top:32px;width:105px;height:259px;background:linear-gradient(180deg,#d9e3e8 0%,#a9b4ba 45%,#2e3a42 100%);opacity:.9}
  .poster .headline{position:absolute;left:76px;top:50px;text-align:right;width:102px}
  .headline .lead{font-size:12.5px;font-weight:500;color:var(--brand-dark);letter-spacing:.3px;white-space:nowrap}
  .headline .big{font-size:26px;font-weight:800;color:var(--brand-blue);line-height:24px;display:block}
  .headline .mid{font-size:17.5px;font-weight:800;color:var(--brand-blue);line-height:20px;display:block}
  .headline .dark{display:inline-block;margin-top:6px;background:var(--brand-dark);color:#fff;font-weight:700;font-size:22px;padding:1px 6px;line-height:25px}
  .services{position:absolute;left:37px;top:155px;list-style:none}
  .services li{position:relative;height:22px;margin-bottom:7.5px;display:flex;align-items:center}
  .services .icon{width:22px;height:22px;border-radius:50%;background:var(--brand-dark);position:relative;z-index:1;display:flex;align-items:center;justify-content:center}
  .services .pill{margin-left:-8px;width:72px;height:14px;background:var(--brand-blue);border-radius:0 7px 7px 0;color:#fff;font-size:7px;font-weight:700;padding-left:14px;line-height:14px}
  .poster .url{position:absolute;left:37px;top:248px;font-size:8px;letter-spacing:3px;color:var(--brand-dark)}
  .url b{color:var(--brand-blue);font-weight:600}

  /* Towers */
  .tower{top:57px;width:97px;height:377px}
  .tower-one{left:464px}
  .tower-two{left:565px}
  .tower-text{position:absolute;left:0;width:97px;text-align:center;color:#fff}
  .tower-text.wordmark{color:var(--brand-blue)}

  /* Back wall */
  .back-wall{left:694px;top:183px;width:467px;height:196px}
  .back-wall .wordmark{position:absolute;transform:translateX(-50%)}
</style>
</head>
<body>

  <section class="piece side-banner" aria-label="Side banner">
    <div class="badge">Calculate<br>Experience<br>Mods<br>Nationwide</div>
  </section>

  <section class="piece header-sign" aria-label="Header sign">
    <span class="wordmark">trelvix</span>
  </section>

  <section class="piece poster" aria-label="Main poster">
    <div class="photo" role="img" aria-label="Photo of a businessman climbing stairs toward bright light"></div>
    <div class="headline">
      <div class="lead">BRING OUT THE</div>
      <span class="big">SUPER</span>
      <span class="mid">PRODUCER</span>
      <span class="dark">IN YOU!</span>
    </div>
    <ul class="services">
      <li><span class="icon"><svg width="11" height="11" viewBox="0 0 11 11"><rect x="1" y="1.5" width="9" height="6" fill="none" stroke="#fff" stroke-width=".9"/><path d="M4 10h3M5.5 7.5v2.5" stroke="#fff" stroke-width=".9"/></svg></span><span class="pill">SOFTWARE</span></li>
      <li><span class="icon"><svg width="11" height="11" viewBox="0 0 11 11"><rect x="2.5" y="1" width="6.5" height="9" fill="none" stroke="#fff" stroke-width=".9"/><path d="M4 3.5h3.5M4 5.5h3.5M4 7.5h2" stroke="#fff" stroke-width=".7"/></svg></span><span class="pill">CLAIMS</span></li>
      <li><span class="icon"><svg width="11" height="11" viewBox="0 0 11 11"><path d="M1 5.5a4.5 4.5 0 0 1 9 0z" fill="none" stroke="#fff" stroke-width=".9"/><path d="M5.5 5.5v3.5a1 1 0 0 1-2 0" fill="none" stroke="#fff" stroke-width=".9"/></svg></span><span class="pill">MARKETS</span></li>
    </ul>
    <div class="url">www.<b>trel</b>vix.com</div>
  </section>

  <section class="piece monitor" aria-label="Display monitor">
    <div class="screen">
      <span class="wordmark">trelvix</span>
      <span class="url">www.trelvix.com</span>
    </div>
  </section>

  <section class="piece tower tower-one" aria-label="Tablet stand">
    <svg width="97" height="377" viewBox="0 0 97 377">
      <defs>
        <clipPath id="tower-shape-a"><path d="M20 0H77Q97 0 97 20C97 60 82 120 82 188C82 256 97 316 97 357Q97 377 77 377H20Q0 377 0 357C0 316 15 256 15 188C15 120 0 60 0 20Q0 0 20 0Z"/></clipPath>
      </defs>
      <g clip-path="url(#tower-shape-a)">
        <rect width="97" height="377" fill="var(--panel-white)"/>
        <path d="M0 30Q48 60 97 30V260Q48 245 0 260Z" fill="var(--brand-blue)"/>
        <path d="M97 95Q30 120 40 260H97Z" fill="var(--brand-blue-light)" opacity=".6"/>
      </g>
    </svg>
    <div class="tower-text wordmark" style="top:18px;font-size:11px">trelvix</div>
    <div role="img" aria-label="Tablet showing hands typing on a keyboard" style="position:absolute;left:13px;top:33px;width:72px;height:48px;background:linear-gradient(135deg,#8fa0ad,#2c3339);border:2px solid #16181a;border-radius:2px"></div>
    <div class="tower-text" style="top:114px;font-family:'Oswald',sans-serif;font-weight:500;font-size:11px;line-height:12px">AUTOMATED</div>
    <div class="tower-text" style="top:126px;font-family:'Oswald',sans-serif;font-weight:600;font-size:22px;line-height:22px">SALES</div>
    <div class="tower-text" style="top:148px;font-weight:700;font-size:9px;line-height:11px">PROCESS<br>TIMELINE</div>
    <div class="tower-text" style="top:227px;font-size:6px">www.<b>trelvix</b>.com</div>
  </section>

  <section class="piece tower tower-two" aria-label="Stand">
    <svg width="97" height="377" viewBox="0 0 97 377">
      <defs>
        <clipPath id="tower-shape-b"><path d="M20 0H77Q97 0 97 20C97 60 82 120 82 188C82 256 97 316 97 357Q97 377 77 377H20Q0 377 0 357C0 316 15 256 15 188C15 120 0 60 0 20Q0 0 20 0Z"/></clipPath>
      </defs>
      <g clip-path="url(#tower-shape-b)">
        <rect width="97" height="377" fill="var(--panel-white)"/>
        <path d="M0 48Q48 70 97 48V252Q48 240 0 252Z" fill="var(--brand-blue)"/>
        <path d="M0 150Q70 170 60 252H0Z" fill="var(--brand-blue-light)" opacity=".5"/>
      </g>
    </svg>
    <div class="tower-text wordmark" style="top:317px;font-size:12px">trelvix</div>
  </section>

  <section class="piece back-wall" aria-label="Booth back wall">
    <svg width="467" height="196" viewBox="0 0 467 196">
      <rect width="467" height="196" fill="var(--panel-white)"/>
      <path d="M0 88Q233 135 467 90V196H0Z" fill="#b8bbbe"/>
      <path d="M0 96Q233 130 467 100V196H0Z" fill="var(--brand-blue)"/>
      <g fill="none" stroke="#e07a4a" stroke-width=".6" stroke-dasharray="2 2">
        <rect x="87" y="24" width="60" height="147"/>
        <rect x="167" y="24" width="134" height="147"/>
        <rect x="319" y="24" width="61" height="147"/>
      </g>
      <rect x="193" y="143" width="81" height="9" rx="4.5" fill="none" stroke="#fff" stroke-width=".8"/>
      <text x="233.5" y="150" text-anchor="middle" fill="#fff" font-family="Montserrat,sans-serif" font-size="5" letter-spacing="1.5">www.<tspan font-weight="700">trelvix</tspan>.com</text>
    </svg>
    <span class="wordmark" style="left:117px;top:77px;font-size:9px">trelvix</span>
    <span class="wordmark" style="left:233px;top:73px;font-size:15px">trelvix</span>
    <span class="wordmark" style="left:349px;top:77px;font-size:9px">trelvix</span>
  </section>

</body>
</html>
```